House-share and Room Rental Website (With Focus on the Bedroom Landing Page)

Looking for website design for our House-share (executive accommodation) and room rental business.

Our company name is: Lodvenra could also be written as LodVenra or lodvenra. Either is fine .. just looking for a nice clean catchy logo to go with the design.

EXAMPLES
These are examples of other websites in this field that are doing well. this is a kind of baseline.
https://kelbrin.com.au/
https://www.tuvaplex.com/
https://www.nestorvi.com/
https://www.quillsa.net/
https://www.pendlebarrow.com.au/

Our business model is to rent rooms to people looking for high-quality accommodation. We fill the gap between those looking to rent rooms and those with rooms to rent. However, our model is slightly different from those already on the market as we looking to fill a massive gap in the market delivering upmarket rooms for rent.(Executive Accommodation) also in the back end will be coupled with a self management process in the back end.

We offer executive style accommodation that stands out above the rest. With special extras like fire safety.. and management processes that create happier homes. We are looking for a web design package that can help us grow and scale our business. We need a design that is captivating

Our MAIN focus is having a room landing page that stands out from the rest... The core of our business will rely on the promotion of the rooms in a share house... so the whole design relies on the BEDROOM landing page to drive results.

Target Market(s)

We have 2 markets we are aiming at ... the first market is people offering rooms to rent who want the highest rental return. The second market is people looking to rent safe, high-quality rooms, in houses that are well managed and looked after.

Industry/Entity Type

Share Economy

Logo Text

LodVenra

Number of Pages Required

5+ page

Font styles to use
Sans Serif

Colors
3276b5

Requirements
Must have
• A messaging system whereby we can create direct communication between those offering rooms and those looking for rooms.
• A call to action that says " Schedule an Inspection"
• Landing page for promoting rooms
• A home page for showing stock.
• Profile page for those selling rooms
• Profile page for those looking for rooms.
• A scheduling calendar for booking inspections
Nice to have
• Pages where new residents can lock in a room.. pay bond and rents.. and sign contracts
• Notifications
• SMS capabilities in the backend.
Should not have
• No script or handwriting fonts.

```html
<!DOCTYPE html>
<html lang="en">
<head>
<meta charset="utf-8">
<title>Lodvenra — Executive Accommodation</title>
<link href="https://fonts.googleapis.com/css2?family=Lato:wght@400;700;900&display=swap" rel="stylesheet">
<style>
:root{
  --blue:#1474c4;
  --blue-dark:#0f5fa3;
  --ink:#1d1d1d;
  --muted:#555;
  --soft:#f5f5f5;
  --line:#dcdcdc;
  --footer:#222;
  --footer-field:#3a3a3a;
  --white:#fff;
}
*{box-sizing:border-box;margin:0;padding:0}
html,body{width:1200px;height:3364px;overflow:hidden}
body{position:relative;font-family:'Lato',sans-serif;color:var(--ink);background:var(--soft)}
.abs{position:absolute}
.center{text-align:center}
svg{display:block}

/* header */
.site-header{left:0;top:0;width:1200px;height:98px;background:var(--white)}
.menu-grid{left:78px;top:38px}
.lang{left:120px;top:38px;font-size:12px;display:flex;align-items:center;gap:6px}
.lang .flag{width:16px;height:11px;background:linear-gradient(#b22 0 50%,#fff 50% 100%);border:1px solid #ccc}
.brand{left:510px;top:24px;display:flex;align-items:center;gap:8px}
.brand .mark{width:40px;height:40px;border-radius:50%;background:var(--blue)}
.brand .name{font-size:30px;font-weight:700;color:var(--blue);line-height:1}
.brand .tag{font-size:10px;color:var(--ink);font-weight:700;margin-top:2px}
.btn-post{left:918px;top:31px;width:128px;height:28px;background:var(--blue);color:#fff;border-radius:4px;font-size:11px;display:flex;align-items:center;justify-content:center}
.btn-login{left:1056px;top:31px;width:62px;height:28px;border:1px solid #bbb;border-radius:4px;font-size:11px;display:flex;align-items:center;justify-content:center;background:#fff}

/* hero */
.hero{left:0;top:98px;width:1200px;height:555px;background:linear-gradient(110deg,#c48a5c 0%,#e3b68c 30%,#d9a479 55%,#9b6a45 80%,#c6926a 100%)}
.hero-title{left:229px;top:345px;font-size:32px;font-weight:700;color:#fff;line-height:42px}
.hero-arrow{top:360px;color:#fff;font-size:22px}
.search-card{left:790px;top:202px;width:327px;height:359px;background:#fff;border-radius:4px;padding:24px 26px;box-shadow:0 4px 16px rgba(0,0,0,.15)}
.search-card h3{font-size:18px;font-weight:700;text-align:center;margin-bottom:14px}
.field-label{font-size:11px;color:var(--muted);margin:8px 0 4px}
.field{height:28px;border:1px solid var(--line);border-radius:3px;font-size:11px;padding:0 10px;display:flex;align-items:center;justify-content:space-between;color:var(--ink)}
.row2{display:flex;gap:14px}
.row2>div{flex:1}
.btn-search{margin-top:14px;height:34px;background:var(--blue);color:#fff;border-radius:4px;font-size:12px;display:flex;align-items:center;justify-content:center}

/* amenities */
.section-title{left:0;width:1200px;text-align:center;font-size:31px;font-weight:700}
.amenity{width:200px;text-align:center}
.amenity .icon{width:82px;height:82px;border-radius:50%;background:var(--blue);margin:0 auto;display:flex;align-items:center;justify-content:center}
.amenity h4{font-size:18px;font-weight:400;margin-top:18px}
.amenity p{font-size:11px;line-height:15px;color:var(--muted);margin-top:14px;padding:0 20px}
.amenity .go{margin:16px auto 0;width:22px;height:22px}

/* tabs */
.tab{width:100px;text-align:center;font-size:17px;color:#333}
.tab svg{margin:0 auto 10px}
.tab.active{color:var(--blue)}

/* room cards */
.room-card{width:325px;height:418px;background:#fff;box-shadow:0 2px 8px rgba(0,0,0,.08)}
.room-photo{position:relative;height:213px}
.room-photo .check{position:absolute;left:8px;top:8px;width:18px;height:18px;border:2px solid rgba(255,255,255,.8);border-radius:2px}
.price{position:absolute;left:0;top:155px;background:var(--blue);color:#fff;font-size:20px;font-weight:700;padding:0 12px 0 8px;height:38px;line-height:38px}
.room-title{font-size:14px;color:var(--blue);padding:24px 18px 0;font-weight:700}
.room-rule{height:1px;background:#eee;margin:12px 0 0}
.room-addr{font-size:13px;color:#333;padding:12px 18px 0;display:flex;align-items:center;gap:8px}
.room-specs{display:flex;justify-content:space-between;padding:14px 28px 0 36px}
.spec{font-size:11px;color:var(--muted);text-align:center}
.spec .ico{display:flex;align-items:flex-end;gap:3px;justify-content:center;height:18px;font-size:11px;color:#222}
.btn-browse{width:104px;height:28px;margin:12px auto 0;background:#3a3a3a;color:#fff;font-size:11px;border-radius:4px;display:flex;align-items:center;justify-content:center}
.btn-more{left:538px;top:2214px;width:126px;height:28px;background:var(--blue);color:#fff;font-size:12px;border-radius:4px;display:flex;align-items:center;justify-content:center}

/* testimonials */
.eyebrow{left:0;width:1200px;text-align:center;font-size:13px}
.testimonial{width:292px;height:290px;background:#fff;text-align:center;padding-top:31px}
.avatar{width:100px;height:100px;border-radius:50%;margin:0 auto;background:radial-gradient(circle at 50% 40%,#b08a72,#4d3b33)}
.testimonial h5{font-size:16px;font-weight:700;margin-top:18px}
.testimonial .role{font-size:12px;color:var(--blue);margin-top:2px}
.testimonial p{font-size:11px;line-height:15px;color:var(--muted);margin:12px auto 0;width:190px}
.read-more{font-size:12px;color:#333;margin-top:18px;display:flex;align-items:center;justify-content:center;gap:5px}

/* newsletter */
.news-title{left:0;width:1200px;text-align:center;font-size:26px;font-weight:400}
.news-sub{left:0;width:1200px;text-align:center;font-size:12px;color:#444}
.news-input{left:336px;top:2858px;width:440px;height:38px;background:#fff;font-size:12px;color:#888;padding:0 16px;display:flex;align-items:center}
.news-submit{left:772px;top:2858px;width:134px;height:38px;background:var(--blue);color:#fff;font-size:13px;display:flex;align-items:center;justify-content:center}

/* footer */
.site-footer{left:0;top:2956px;width:1200px;height:350px;background:var(--footer);color:#ddd}
.f-brand{left:79px;top:3045px;display:flex;align-items:center;gap:8px}
.f-brand .mark{width:36px;height:36px;border-radius:50%;background:var(--blue)}
.f-brand .name{font-size:28px;font-weight:700;color:var(--blue);line-height:1}
.f-brand .tag{font-size:10px;color:#ddd}
.f-about{left:79px;top:3118px;width:220px;font-size:13px;line-height:20px;color:#ddd}
.socials{left:79px;top:3209px;display:flex;gap:10px}
.socials span{width:22px;height:22px;border-radius:50%;border:1px solid #ddd}
.socials span:first-child{background:var(--blue);border-color:var(--blue)}
.f-head{font-size:16px;color:#fff}
.f-head::after{content:"";display:block;width:90px;height:2px;background:#ddd;margin-top:8px}
.f-links{list-style:none;font-size:11px;line-height:24px}
.f-links li::before{content:"›";margin-right:16px;font-size:14px}
.f-contact{font-size:13px;line-height:20px}
.f-contact .item{display:flex;gap:10px;margin-bottom:12px}
.qc-field{height:28px;background:var(--footer-field);border:1px solid #555;font-size:12px;color:#ccc;padding:5px 12px}
.qc-send{background:var(--blue);color:#fff;font-size:12px;display:flex;align-items:center;justify-content:center;border-radius:3px}
.bottom-bar{left:0;top:3306px;width:1200px;height:58px;background:var(--blue);color:#fff;font-size:13px}
.pay{width:30px;height:20px;background:#fff;border-radius:2px}
</style>
</head>
<body>

<header class="abs site-header">
  <svg class="abs menu-grid" width="24" height="24" viewBox="0 0 24 24" fill="#333">
    <rect x="0" y="0" width="5" height="5"/><rect x="9" y="0" width="5" height="5"/><rect x="18" y="0" width="5" height="5"/>
    <rect x="0" y="9" width="5" height="5"/><rect x="9" y="9" width="5" height="5"/><rect x="18" y="9" width="5" height="5"/>
    <rect x="0" y="18" width="5" height="5"/><rect x="9" y="18" width="5" height="5"/><rect x="18" y="18" width="5" height="5"/>
  </svg>
  <div class="abs lang"><span class="flag"></span>Eng ▾</div>
  <div class="abs brand">
    <span class="mark"></span>
    <div><div class="name">Lodvenra</div><div class="tag">Executive Accommodation</div></div>
  </div>
  <div class="abs btn-post">Post Your Room</div>
  <div class="abs btn-login">Log in</div>
</header>

<section class="abs hero" role="img" aria-label="Photo of an elegant bedroom with a canopy bed and a blue chaise longue"></section>
<div class="abs hero-arrow" style="left:30px">‹</div>
<div class="abs hero-arrow" style="left:1150px">›</div>
<h1 class="abs hero-title">let us find Your Perfect<br>Room For Rent</h1>

<form class="abs search-card">
  <h3>Find Your Room For Rent</h3>
  <div class="field-label">Where</div>
  <div class="field">Anywhere
    <svg width="12" height="14" viewBox="0 0 12 14"><path d="M6 1a4.5 4.5 0 0 0-4.5 4.5C1.5 9 6 13 6 13s4.5-4 4.5-7.5A4.5 4.5 0 0 0 6 1z" fill="none" stroke="#777"/><circle cx="6" cy="5.5" r="1.6" fill="#777"/></svg>
  </div>
  <div class="row2">
    <div><div class="field-label">Check in</div><div class="field"><span></span><svg width="13" height="13" viewBox="0 0 13 13"><rect x="1" y="2" width="11" height="10" fill="none" stroke="#777"/><path d="M1 5h11M4 1v2M9 1v2" stroke="#777"/></svg></div></div>
    <div><div class="field-label">Check out</div><div class="field"><span></span><svg width="13" height="13" viewBox="0 0 13 13"><rect x="1" y="2" width="11" height="10" fill="none" stroke="#777"/><path d="M1 5h11M4 1v2M9 1v2" stroke="#777"/></svg></div></div>
  </div>
  <div class="field-label">Category</div>
  <div class="field">Room For Rent <span>▾</span></div>
  <div class="field" style="margin-top:12px">Guests <span>▾</span></div>
  <div class="btn-search">Search</div>
</form>

<h2 class="abs section-title" style="top:708px">Public Amenities</h2>

<div class="abs amenity" style="left:59px;top:785px">
  <div class="icon"><svg width="40" height="30" viewBox="0 0 40 30" fill="#fff"><path d="M8 4h24l5 10v12h-5v-4H8v4H3V14z"/><rect x="10" y="7" width="20" height="7" fill="#1474c4"/><circle cx="10" cy="18" r="2.5" fill="#1474c4"/><circle cx="30" cy="18" r="2.5" fill="#1474c4"/></svg></div>
  <h4>Transport</h4><p>Lorem Ipsum is simply is a text of the printinghas been ndustry's 1500s...</p>
  <svg class="go" viewBox="0 0 22 22"><circle cx="11" cy="11" r="9.5" fill="none" stroke="#333" stroke-width="1.5"/><path d="M6 11h9M12 7.5l3.5 3.5-3.5 3.5" fill="none" stroke="#333" stroke-width="1.5"/></svg>
</div>
<div class="abs amenity" style="left:286px;top:785px">
  <div class="icon"><svg width="30" height="36" viewBox="0 0 30 36" fill="#fff"><rect x="3" y="2" width="24" height="26" rx="5"/><rect x="7" y="7" width="16" height="9" fill="#1474c4"/><circle cx="9" cy="22" r="2" fill="#1474c4"/><circle cx="21" cy="22" r="2" fill="#1474c4"/><path d="M7 28l-4 6M23 28l4 6" stroke="#fff" stroke-width="2.5"/></svg></div>
  <h4>Trains</h4><p>Lorem Ipsum is simply is a text of the printinghas been ndustry's 1500s...</p>
  <svg class="go" viewBox="0 0 22 22"><circle cx="11" cy="11" r="9.5" fill="none" stroke="#333" stroke-width="1.5"/><path d="M6 11h9M12 7.5l3.5 3.5-3.5 3.5" fill="none" stroke="#333" stroke-width="1.5"/></svg>
</div>
<div class="abs amenity" style="left:501px;top:785px">
  <div class="icon"><svg width="32" height="36" viewBox="0 0 32 36" fill="#fff"><rect x="3" y="2" width="26" height="28" rx="4"/><rect x="7" y="7" width="18" height="10" fill="#1474c4"/><circle cx="9" cy="23" r="2" fill="#1474c4"/><circle cx="23" cy="23" r="2" fill="#1474c4"/><rect x="5" y="30" width="5" height="5"/><rect x="22" y="30" width="5" height="5"/></svg></div>
  <h4>Busses</h4><p>Lorem Ipsum is simply is a text of the printinghas been ndustry's 1500s...</p>
  <svg class="go" viewBox="0 0 22 22"><circle cx="11" cy="11" r="9.5" fill="none" stroke="#333" stroke-width="1.5"/><path d="M6 11h9M12 7.5l3.5 3.5-3.5 3.5" fill="none" stroke="#333" stroke-width="1.5"/></svg>
</div>
<div class="abs amenity" style="left:716px;top:785px">
  <div class="icon"><svg width="36" height="38" viewBox="0 0 36 38"><circle cx="18" cy="20" r="15" fill="none" stroke="#fff" stroke-width="2.5"/><path d="M18 3a7 7 0 0 0-7 7c0 6 7 13 7 13s7-7 7-13a7 7 0 0 0-7-7z" fill="#fff"/><circle cx="18" cy="10" r="2.5" fill="#1474c4"/></svg></div>
  <h4>Location</h4><p>Lorem Ipsum is simply is a text of the printinghas been ndustry's 1500s...</p>
  <svg class="go" viewBox="0 0 22 22"><circle cx="11" cy="11" r="9.5" fill="none" stroke="#333" stroke-width="1.5"/><path d="M6 11h9M12 7.5l3.5 3.5-3.5 3.5" fill="none" stroke="#333" stroke-width="1.5"/></svg>
</div>
<div class="abs amenity" style="left:936px;top:785px">
  <div class="icon"><svg width="38" height="32" viewBox="0 0 38 32"><path d="M2 4l11-3 12 3 11-3v27l-11 3-12-3-11 3z" fill="none" stroke="#fff" stroke-width="2.5" stroke-linejoin="round"/><path d="M13 1v27M25 4v27" stroke="#fff" stroke-width="2"/></svg></div>
  <h4>MAP</h4><p>Lorem Ipsum is simply is a text of the printinghas been ndustry's 1500s...</p>
  <svg class="go" viewBox="0 0 22 22"><circle cx="11" cy="11" r="9.5" fill="none" stroke="#333" stroke-width="1.5"/><path d="M6 11h9M12 7.5l3.5 3.5-3.5 3.5" fill="none" stroke="#333" stroke-width="1.5"/></svg>
</div>

<h2 class="abs section-title" style="top:1074px">Recommended for you</h2>

<div class="abs tab" style="left:257px;top:1156px">
  <svg width="36" height="36" viewBox="0 0 36 36" fill="#333"><rect x="2" y="2" width="8" height="8"/><rect x="14" y="2" width="8" height="8"/><rect x="26" y="2" width="8" height="8"/><rect x="2" y="14" width="8" height="8"/><rect x="14" y="14" width="8" height="8"/><rect x="26" y="14" width="8" height="8"/><rect x="2" y="26" width="8" height="8"/><rect x="14" y="26" width="8" height="8"/><rect x="26" y="26" width="8" height="8"/></svg>All</div>
<div class="abs tab active" style="left:403px;top:1150px">
  <svg width="36" height="42" viewBox="0 0 36 42"><path d="M6 40V3h24v37" fill="none" stroke="#1474c4" stroke-width="2.5"/><path d="M9 4l14 4v32L9 38z" fill="#1474c4"/><circle cx="19" cy="23" r="1.5" fill="#fff"/></svg>Room</div>
<div class="abs tab" style="left:549px;top:1152px">
  <svg width="42" height="40" viewBox="0 0 42 40" fill="#333"><path d="M21 2L1 20h6v18h10V26h8v12h10V20h6z"/></svg>House</div>
<div class="abs tab" style="left:697px;top:1154px">
  <svg width="44" height="38" viewBox="0 0 44 38" fill="none" stroke="#333" stroke-width="2.5"><path d="M3 2v34M41 2v34M3 15h38M3 29h38"/><rect x="8" y="7" width="10" height="6" fill="#333"/><rect x="8" y="21" width="10" height="6" fill="#333"/></svg>Roomate</div>
<div class="abs tab" style="left:845px;top:1152px">
  <svg width="40" height="40" viewBox="0 0 40 40" fill="#333"><path d="M20 2L3 16v22h34V16z"/><circle cx="20" cy="17" r="4" fill="#fff"/><path d="M13 34c0-7 3-10 7-10s7 3 7 10z" fill="#fff"/></svg>Tenant</div>

<!-- room cards -->
<article class="abs room-card" style="left:81px;top:1276px">
  <div class="room-photo" role="img" aria-label="Photo of a bright bedroom with chandelier and tall windows" style="background:linear-gradient(135deg,#cfc3ad,#8a7f6e 60%,#b3a68e)"><span class="check"></span><span class="price">$250</span></div>
  <div class="room-title">Luxurious &amp; Stunning Room</div><div class="room-rule"></div>
  <div class="room-addr"><svg width="11" height="14" viewBox="0 0 12 14"><path d="M6 1a4.5 4.5 0 0 0-4.5 4.5C1.5 9 6 13 6 13s4.5-4 4.5-7.5A4.5 4.5 0 0 0 6 1z" fill="none" stroke="#555"/><circle cx="6" cy="5.5" r="1.5" fill="#555"/></svg>43 Kestrel Road,Marlowe, Australia</div>
  <div class="room-specs">
    <div class="spec"><div class="ico"><svg width="18" height="16" viewBox="0 0 18 16" fill="#333"><path d="M9 1L1 7v8h16V7z"/></svg>2</div>Rooms</div>
    <div class="spec"><div class="ico"><svg width="22" height="14" viewBox="0 0 22 14" fill="#333"><rect x="1" y="5" width="20" height="6"/><rect x="1" y="1" width="6" height="4"/><rect x="1" y="11" width="2" height="3"/><rect x="19" y="11" width="2" height="3"/></svg>4</div>Bedrooms</div>
    <div class="spec"><div class="ico"><svg width="18" height="16" viewBox="0 0 18 16" fill="#333"><rect x="1" y="7" width="16" height="5" rx="1"/><path d="M3 7V2h3" stroke="#333" fill="none" stroke-width="1.5"/><rect x="3" y="12" width="2" height="3"/><rect x="13" y="12" width="2" height="3"/></svg>2</div>Bath</div>
  </div>
  <div class="btn-browse">Browse</div>
</article>
<article class="abs room-card" style="left:435px;top:1276px">
  <div class="room-photo" role="img" aria-label="Photo of a classic bedroom with a red canopy bed" style="background:linear-gradient(135deg,#d9b89b,#a6513f 55%,#c99c7a)"><span class="check"></span><span class="price">$250</span></div>
  <div class="room-title">Luxurious &amp; Stunning Room</div><div class="room-rule"></div>
  <div class="room-addr"><svg width="11" height="14" viewBox="0 0 12 14"><path d="M6 1a4.5 4.5 0 0 0-4.5 4.5C1.5 9 6 13 6 13s4.5-4 4.5-7.5A4.5 4.5 0 0 0 6 1z" fill="none" stroke="#555"/><circle cx="6" cy="5.5" r="1.5" fill="#555"/></svg>43 Kestrel Road,Marlowe, Australia</div>
  <div class="room-specs">
    <div class="spec"><div class="ico"><svg width="18" height="16" viewBox="0 0 18 16" fill="#333"><path d="M9 1L1 7v8h16V7z"/></svg>2</div>Rooms</div>
    <div class="spec"><div class="ico"><svg width="22" height="14" viewBox="0 0 22 14" fill="#333"><rect x="1" y="5" width="20" height="6"/><rect x="1" y="1" width="6" height="4"/><rect x="1" y="11" width="2" height="3"/><rect x="19" y="11" width="2" height="3"/></svg>4</div>Bedrooms</div>
    <div class="spec"><div class="ico"><svg width="18" height="16" viewBox="0 0 18 16" fill="#333"><rect x="1" y="7" width="16" height="5" rx="1"/><path d="M3 7V2h3" stroke="#333" fill="none" stroke-width="1.5"/><rect x="3" y="12" width="2" height="3"/><rect x="13" y="12" width="2" height="3"/></svg>2</div>Bath</div>
  </div>
  <div class="btn-browse">Browse</div>
</article>
<article class="abs room-card" style="left:794px;top:1276px">
  <div class="room-photo" role="img" aria-label="Photo of a spacious bedroom with a bay window" style="background:linear-gradient(135deg,#e2d6c0,#9c7a5c 55%,#c7b294)"><span class="check"></span><span class="price">$250</span></div>
  <div class="room-title">Luxurious &amp; Stunning Room</div><div class="room-rule"></div>
  <div class="room-addr"><svg width="11" height="14" viewBox="0 0 12 14"><path d="M6 1a4.5 4.5 0 0 0-4.5 4.5C1.5 9 6 13 6 13s4.5-4 4.5-7.5A4.5 4.5 0 0 0 6 1z" fill="none" stroke="#555"/><circle cx="6" cy="5.5" r="1.5" fill="#555"/></svg>43 Kestrel Road,Marlowe, Australia</div>
  <div class="room-specs">
    <div class="spec"><div class="ico"><svg width="18" height="16" viewBox="0 0 18 16" fill="#333"><path d="M9 1L1 7v8h16V7z"/></svg>2</div>Rooms</div>
    <div class="spec"><div class="ico"><svg width="22" height="14" viewBox="0 0 22 14" fill="#333"><rect x="1" y="5" width="20" height="6"/><rect x="1" y="1" width="6" height="4"/><rect x="1" y="11" width="2" height="3"/><rect x="19" y="11" width="2" height="3"/></svg>4</div>Bedrooms</div>
    <div class="spec"><div class="ico"><svg width="18" height="16" viewBox="0 0 18 16" fill="#333"><rect x="1" y="7" width="16" height="5" rx="1"/><path d="M3 7V2h3" stroke="#333" fill="none" stroke-width="1.5"/><rect x="3" y="12" width="2" height="3"/><rect x="13" y="12" width="2" height="3"/></svg>2</div>Bath</div>
  </div>
  <div class="btn-browse">Browse</div>
</article>

<article class="abs room-card" style="left:81px;top:1741px">
  <div class="room-photo" role="img" aria-label="Photo of a white canopy bed with orange cushions" style="background:linear-gradient(135deg,#f1ede6,#d8cfc3 55%,#c98d5a)"><span class="check"></span><span class="price">$250</span></div>
  <div class="room-title">Luxurious &amp; Stunning Room</div><div class="room-rule"></div>
  <div class="room-addr"><svg width="11" height="14" viewBox="0 0 12 14"><path d="M6 1a4.5 4.5 0 0 0-4.5 4.5C1.5 9 6 13 6 13s4.5-4 4.5-7.5A4.5 4.5 0 0 0 6 1z" fill="none" stroke="#555"/><circle cx="6" cy="5.5" r="1.5" fill="#555"/></svg>43 Kestrel Road,Marlowe, Australia</div>
  <div class="room-specs">
    <div class="spec"><div class="ico"><svg width="18" height="16" viewBox="0 0 18 16" fill="#333"><path d="M9 1L1 7v8h16V7z"/></svg>2</div>Rooms</div>
    <div class="spec"><div class="ico"><svg width="22" height="14" viewBox="0 0 22 14" fill="#333"><rect x="1" y="5" width="20" height="6"/><rect x="1" y="1" width="6" height="4"/><rect x="1" y="11" width="2" height="3"/><rect x="19" y="11" width="2" height="3"/></svg>4</div>Bedrooms</div>
    <div class="spec"><div class="ico"><svg width="18" height="16" viewBox="0 0 18 16" fill="#333"><rect x="1" y="7" width="16" height="5" rx="1"/><path d="M3 7V2h3" stroke="#333" fill="none" stroke-width="1.5"/><rect x="3" y="12" width="2" height="3"/><rect x="13" y="12" width="2" height="3"/></svg>2</div>Bath</div>
  </div>
  <div class="btn-browse">Browse</div>
</article>
<article class="abs room-card" style="left:435px;top:1741px">
  <div class="room-photo" role="img" aria-label="Photo of a bedroom with carved dark wooden panels" style="background:linear-gradient(135deg,#5a4436,#2f241d 50%,#8b7565)"><span class="check"></span><span class="price">$250</span></div>
  <div class="room-title">Luxurious &amp; Stunning Room</div><div class="room-rule"></div>
  <div class="room-addr"><svg width="11" height="14" viewBox="0 0 12 14"><path d="M6 1a4.5 4.5 0 0 0-4.5 4.5C1.5 9 6 13 6 13s4.5-4 4.5-7.5A4.5 4.5 0 0 0 6 1z" fill="none" stroke="#555"/><circle cx="6" cy="5.5" r="1.5" fill="#555"/></svg>43 Kestrel Road,Marlowe, Australia</div>
  <div class="room-specs">
    <div class="spec"><div class="ico"><svg width="18" height="16" viewBox="0 0 18 16" fill="#333"><path d="M9 1L1 7v8h16V7z"/></svg>2</div>Rooms</div>
    <div class="spec"><div class="ico"><svg width="22" height="14" viewBox="0 0 22 14" fill="#333"><rect x="1" y="5" width="20" height="6"/><rect x="1" y="1" width="6" height="4"/><rect x="1" y="11" width="2" height="3"/><rect x="19" y="11" width="2" height="3"/></svg>4</div>Bedrooms</div>
    <div class="spec"><div class="ico"><svg width="18" height="16" viewBox="0 0 18 16" fill="#333"><rect x="1" y="7" width="16" height="5" rx="1"/><path d="M3 7V2h3" stroke="#333" fill="none" stroke-width="1.5"/><rect x="3" y="12" width="2" height="3"/><rect x="13" y="12" width="2" height="3"/></svg>2</div>Bath</div>
  </div>
  <div class="btn-browse">Browse</div>
</article>
<article class="abs room-card" style="left:794px;top:1741px">
  <div class="room-photo" role="img" aria-label="Photo of a red-toned bedroom with an ornate sofa" style="background:linear-gradient(135deg,#d98f7c,#a8352c 55%,#e0b49a)"><span class="check"></span><span class="price">$250</span></div>
  <div class="room-title">Luxurious &amp; Stunning Room</div><div class="room-rule"></div>
  <div class="room-addr"><svg width="11" height="14" viewBox="0 0 12 14"><path d="M6 1a4.5 4.5 0 0 0-4.5 4.5C1.5 9 6 13 6 13s4.5-4 4.5-7.5A4.5 4.5 0 0 0 6 1z" fill="none" stroke="#555"/><circle cx="6" cy="5.5" r="1.5" fill="#555"/></svg>43 Kestrel Road,Marlowe, Australia</div>
  <div class="room-specs">
    <div class="spec"><div class="ico"><svg width="18" height="16" viewBox="0 0 18 16" fill="#333"><path d="M9 1L1 7v8h16V7z"/></svg>2</div>Rooms</div>
    <div class="spec"><div class="ico"><svg width="22" height="14" viewBox="0 0 22 14" fill="#333"><rect x="1" y="5" width="20" height="6"/><rect x="1" y="1" width="6" height="4"/><rect x="1" y="11" width="2" height="3"/><rect x="19" y="11" width="2" height="3"/></svg>4</div>Bedrooms</div>
    <div class="spec"><div class="ico"><svg width="18" height="16" viewBox="0 0 18 16" fill="#333"><rect x="1" y="7" width="16" height="5" rx="1"/><path d="M3 7V2h3" stroke="#333" fill="none" stroke-width="1.5"/><rect x="3" y="12" width="2" height="3"/><rect x="13" y="12" width="2" height="3"/></svg>2</div>Bath</div>
  </div>
  <div class="btn-browse">Browse</div>
</article>

<div class="abs btn-more">View More</div>

<!-- testimonials -->
<div class="abs eyebrow" style="top:2307px">Testimonials</div>
<h2 class="abs section-title" style="top:2333px;font-weight:400">What Client Say</h2>

<div class="abs testimonial" style="left:117px;top:2405px">
  <div class="avatar" role="img" aria-label="Client portrait"></div>
  <h5>Christopher</h5><div class="role">Director</div>
  <p>Lorem Ipsum is simply dummy of the printing and typesetting Lorem Ipsum industry.</p>
  <div class="read-more">Read More... <svg width="13" height="13" viewBox="0 0 22 22"><circle cx="11" cy="11" r="9.5" fill="none" stroke="#333" stroke-width="2"/><path d="M6 11h9M12 7.5l3.5 3.5-3.5 3.5" fill="none" stroke="#333" stroke-width="2"/></svg></div>
</div>
<div class="abs testimonial" style="left:453px;top:2405px">
  <div class="avatar" role="img" aria-label="Client portrait" style="background:radial-gradient(circle at 50% 40%,#c9a991,#556a80)"></div>
  <h5>John</h5><div class="role">Director</div>
  <p>Lorem Ipsum is simply dummy of the printing and typesetting Lorem Ipsum industry.</p>
  <div class="read-more">Read More... <svg width="13" height="13" viewBox="0 0 22 22"><circle cx="11" cy="11" r="9.5" fill="none" stroke="#333" stroke-width="2"/><path d="M6 11h9M12 7.5l3.5 3.5-3.5 3.5" fill="none" stroke="#333" stroke-width="2"/></svg></div>
</div>
<div class="abs testimonial" style="left:784px;top:2405px">
  <div class="avatar" role="img" aria-label="Client portrait" style="background:radial-gradient(circle at 50% 40%,#9a7c6b,#2b2320)"></div>
  <h5 style="color:#1a3f9a">Daniel</h5><div class="role">Director</div>
  <p>Lorem Ipsum is simply dummy of the printing and typesetting Lorem Ipsum industry.</p>
  <div class="read-more">Read More... <svg width="13" height="13" viewBox="0 0 22 22"><circle cx="11" cy="11" r="9.5" fill="none" stroke="#333" stroke-width="2"/><path d="M6 11h9M12 7.5l3.5 3.5-3.5 3.5" fill="none" stroke="#333" stroke-width="2"/></svg></div>
</div>

<!-- newsletter -->
<h2 class="abs news-title" style="top:2771px">Subscribe To Our Newsletter</h2>
<div class="abs news-sub" style="top:2814px">To Receive The latest News And Update</div>
<div class="abs news-input">Your E-Mail</div>
<div class="abs news-submit">Submit</div>

<!-- footer -->
<footer class="abs site-footer"></footer>
<div class="abs f-brand">
  <span class="mark"></span>
  <div><div class="name">Lodvenra</div><div class="tag">Executive Accommodation</div></div>
</div>
<p class="abs f-about">Lorem Ipsum is simply dummy text of the printing and types tysletting industry...</p>
<div class="abs socials"><span></span><span></span><span></span><span></span><span></span></div>

<div class="abs" style="left:372px;top:3032px">
  <div class="f-head">Useful links</div>
  <ul class="f-links" style="margin-top:18px">
    <li>Login</li><li>Register</li><li>My Profile</li><li>My Subscription</li><li>Privacy policy</li><li>Terms &amp; Conditions</li>
  </ul>
</div>

<div class="abs f-contact" style="left:577px;top:3032px;width:230px">
  <div class="f-head" style="margin-bottom:22px">Contact us</div>
  <div class="item"><svg width="16" height="16" viewBox="0 0 16 16" fill="#ddd"><path d="M8 1L1 7h2v8h4v-5h2v5h4V7h2z"/></svg><span>14 Wendral Place ,Corvella<br>Western Australia.<br>ZipCode: 60412</span></div>
  <div class="item"><svg width="16" height="16" viewBox="0 0 16 16" fill="#ddd"><path d="M3 1l3 3-2 2c1 2 3 4 5 5l2-2 3 3-2 3C7 15 1 9 1 3z"/></svg><span>08 5550 1947</span></div>
  <div class="item"><svg width="16" height="16" viewBox="0 0 16 16"><rect x="1" y="3" width="14" height="10" fill="none" stroke="#ddd" stroke-width="1.5"/><path d="M1 3l7 6 7-6" fill="none" stroke="#ddd" stroke-width="1.5"/></svg><span>info@lodvenra.com</span></div>
</div>

<div class="abs" style="left:890px;top:3032px">
  <div class="f-head">Quick Contact</div>
</div>
<div class="abs qc-field" style="left:890px;top:3100px;width:113px">Name</div>
<div class="abs qc-field" style="left:1012px;top:3100px;width:107px">Phone</div>
<div class="abs qc-field" style="left:890px;top:3136px;width:229px;height:62px">Message</div>
<div class="abs qc-send" style="left:993px;top:3205px;width:126px;height:28px">Send</div>

<div class="abs bottom-bar">
  <div class="abs" style="left:79px;top:21px">CopyRight © 2019 Lodvenra. All Right Reserve</div>
  <div class="abs" style="left:915px;top:19px;display:flex;gap:9px"><span class="pay"></span><span class="pay"></span><span class="pay"></span><span class="pay"></span><span class="pay"></span></div>
</div>

</body>
</html>
```